"Velmora Kestrel Bridgeworks": unique end to end Chinese marketing and ecommerce solutions*

I would like to create a company website for my trademark: "Velmora Kestrel Bridgeworks". We are based in Iceland. We are the only company in the market offering end-to-end Chinese digital marketing and eCommerce solutions. We help companies grow their brands and sales towards Chinese - whether tourism, export of products or services.
I include the logo that we have come up with in terms of colours and fonts.
The font is Trajan - I would like to use normal letters (capital and lowercase) for text.
Front page: Picture with colour filter. Logo in white. Text line underneath.
I am inspired by this website:
https://www.pelorumgrove.example/
I like these short videos for landing page:
https://www.framelodex.example/video/clip-30417852-ridge-scenic-vista-mountains
https://www.framelodex.example/video/clip-2093847155-4k-aerial-video-ridge-path-vista
https://www.framelodex.example/video/clip-3058172649-ridge-path-vista
Icelandic businesses looking for business opportunities in China or to attract Chinese tourists.
Digital Marketing

```html
<!DOCTYPE html>
<html lang="en">
<head>
<meta charset="utf-8">
<title>Velmora Kestrel Bridgeworks</title>
<link rel="stylesheet" href="https://fonts.googleapis.com/css2?family=Cinzel:wght@400;500&display=swap">
<style>
  :root {
    --page: #ffffff;
    --royal: #0055a8;
    --gold: #b68f52;
    --ink-light: #ffffff;
    --forest-dark: #2f5a22;
    --forest-mid: #4d8a34;
    --forest-light: #7fae57;
  }
  * { margin: 0; padding: 0; box-sizing: border-box; }
  html, body {
    width: 1200px;
    height: 1200px;
    overflow: hidden;
    background: var(--page);
  }
  body {
    position: relative;
    font-family: "Cinzel", "Trajan Pro", serif;
    color: var(--ink-light);
  }
  .site {
    position: absolute;
    left: 65px;
    top: 65px;
    width: 1070px;
    height: 1070px;
  }
  .hero {
    position: absolute;
    left: 0;
    top: 0;
    width: 1070px;
    height: 578px;
    background:
      radial-gradient(ellipse at 55% 40%, rgba(200,190,170,0.35) 0%, rgba(200,190,170,0) 30%),
      linear-gradient(160deg, var(--forest-light) 0%, var(--forest-mid) 35%, var(--forest-dark) 60%, var(--forest-mid) 85%, var(--forest-light) 100%);
  }
  .brand {
    position: absolute;
    left: 32px;
    top: 32px;
    display: flex;
    align-items: center;
    gap: 12px;
  }
  .brand-mark {
    width: 26px;
    height: 26px;
    border-radius: 50%;
    background: var(--ink-light);
  }
  .brand-name {
    font-size: 20px;
    font-weight: 500;
    letter-spacing: 0.5px;
    color: var(--ink-light);
  }
  .top-nav {
    position: absolute;
    right: 30px;
    top: 45px;
    text-align: right;
    font-size: 15px;
    line-height: 22px;
    list-style: none;
  }
  .top-nav li::after {
    content: "";
    display: inline-block;
    margin-left: 10px;
    border-left: 7px solid var(--ink-light);
    border-top: 4.5px solid transparent;
    border-bottom: 4.5px solid transparent;
    vertical-align: 1px;
  }
  .intro {
    position: absolute;
    left: 0;
    top: 582px;
    width: 1070px;
    height: 385px;
    background: var(--royal);
    text-align: center;
    padding-top: 48px;
  }
  .intro p {
    font-size: 25px;
    line-height: 59.5px;
    letter-spacing: 1.2px;
    font-variant: small-caps;
  }
  .footer {
    position: absolute;
    left: 0;
    top: 967px;
    width: 1070px;
    height: 103px;
    background: var(--gold);
    display: flex;
    align-items: center;
    justify-content: center;
    font-size: 14px;
    letter-spacing: 0.3px;
  }
</style>
</head>
<body>
  <div class="site">
    <header class="hero" role="img" aria-label="Aerial view of an ancient stone wall and watchtower winding along forested green mountain ridges">
      <div class="brand">
        <span class="brand-mark"></span>
        <span class="brand-name">Velmora Kestrel Bridgeworks</span>
      </div>
      <ul class="top-nav">
        <li>log in/sign up</li>
        <li>main menu</li>
      </ul>
    </header>
    <section class="intro">
      <p>We are the only company in the market<br>
      offering end-to-end Chinese digital marketing<br>
      and eCommerce solutions.<br>
      We help companies grow their brands and sales towards Chinese<br>
      whether tourism, export of products or services.</p>
    </section>
    <footer class="footer">Velmora Kestrel Bridgeworks 2021</footer>
  </div>
</body>
</html>
```